Business Card Design Project

I have attached the logo and the colour pallete for the branding for the company.

Creative designs for business cards are needed.

The Company is modern corporate.

Industry/Entity Type

Business

```html
<!DOCTYPE html>
<html lang="en">
<head>
<meta charset="utf-8">
<title>Stepwise Business Cards</title>
<link rel="stylesheet" href="https://fonts.googleapis.com/css2?family=Source+Sans+3:wght@400;600;700&display=swap">
<style>
  :root {
    --plum: #5b1f5e;
    --plum-deep: #3a0f3d;
    --plum-light: #7a2d78;
    --orange: #f07a1e;
    --orange-red: #e8452a;
    --ink: #3a3a3a;
    --paper: #ffffff;
    --ground: #eceae6;
    --faint: #f6e4e2;
  }
  * { margin: 0; padding: 0; box-sizing: border-box; }
  html, body { width: 1200px; height: 720px; overflow: hidden; }
  body {
    background: var(--ground);
    font-family: "Source Sans 3", "Myriad Pro", sans-serif;
    position: relative;
  }
  .card {
    position: absolute;
    top: 200px;
    width: 525px;
    height: 300px;
    border-radius: 4px;
    box-shadow: 0 8px 24px rgba(0,0,0,0.18);
    overflow: hidden;
  }
  .card--front { left: 50px; background: var(--paper); }
  .card--back {
    left: 625px;
    background: radial-gradient(ellipse at 55% 40%, var(--plum-light) 0%, var(--plum) 45%, var(--plum-deep) 100%);
    display: flex;
    flex-direction: column;
    align-items: center;
    justify-content: center;
  }
  .brand-name {
    font-weight: 700;
    letter-spacing: -1px;
    line-height: 1;
  }
  .card--front .brand-name {
    position: absolute;
    left: 34px;
    top: 34px;
    font-size: 66px;
    color: var(--plum);
  }
  .card--back .brand-name {
    font-size: 78px;
    color: var(--paper);
    margin-top: -10px;
  }
  .web-line {
    color: var(--paper);
    font-size: 17px;
    letter-spacing: 4px;
    margin-top: 26px;
  }
  .accent-circle {
    position: absolute;
    right: 42px;
    top: 46px;
    width: 90px;
    height: 90px;
    border-radius: 50%;
    background: var(--faint);
  }
  .person {
    position: absolute;
    right: 40px;
    top: 100px;
    text-align: left;
  }
  .person-name {
    color: var(--plum);
    font-weight: 700;
    font-size: 17px;
  }
  .person-title {
    color: var(--orange);
    font-size: 11px;
    text-align: right;
    margin-top: -2px;
  }
  .contact {
    position: absolute;
    left: 40px;
    top: 160px;
    list-style: none;
    color: var(--ink);
    font-size: 13px;
    line-height: 1;
  }
  .contact li {
    display: flex;
    align-items: center;
    gap: 7px;
    margin-bottom: 5px;
  }
  .contact svg { width: 11px; height: 11px; flex: none; }
  .address {
    position: absolute;
    left: 40px;
    top: 252px;
    color: var(--ink);
    font-size: 13px;
    line-height: 1.2;
    font-style: normal;
  }
</style>
</head>
<body>
  <section class="card card--front" aria-label="Business card front">
    <div class="brand-name">stepwise</div>
    <div class="accent-circle" aria-hidden="true"></div>
    <div class="person">
      <div class="person-name">Your Name</div>
      <div class="person-title">Title</div>
    </div>
    <ul class="contact">
      <li>
        <svg viewBox="0 0 12 12" aria-hidden="true"><circle cx="6" cy="6" r="6" fill="var(--orange-red)"/><path d="M4 3.2c.4-.3.8-.2 1 .2l.4.9c.1.3 0 .5-.2.7l-.3.3c.3.7.9 1.3 1.6 1.6l.3-.3c.2-.2.4-.3.7-.2l.9.4c.4.2.5.6.2 1-.6.8-1.6.9-2.6.3A6 6 0 0 1 3.8 5.6c-.5-1-.4-1.8.2-2.4z" fill="#fff"/></svg>
        123-456-0789
      </li>
      <li>
        <svg viewBox="0 0 12 12" aria-hidden="true"><rect x="3" y="0.5" width="6" height="11" rx="1.2" fill="var(--orange-red)"/><rect x="4" y="2" width="4" height="6" fill="#fff"/><circle cx="6" cy="9.7" r=".7" fill="#fff"/></svg>
        123-456-0789
      </li>
      <li>
        <svg viewBox="0 0 12 12" aria-hidden="true"><circle cx="6" cy="6" r="6" fill="var(--orange-red)"/><rect x="2.8" y="3.8" width="6.4" height="4.4" fill="#fff"/><path d="M2.8 3.8 6 6.4l3.2-2.6" fill="none" stroke="var(--orange-red)" stroke-width=".7"/></svg>
        info@stepwise.com
      </li>
      <li>
        <svg viewBox="0 0 12 12" aria-hidden="true"><circle cx="6" cy="6" r="6" fill="var(--orange-red)"/><circle cx="6" cy="6" r="3.5" fill="none" stroke="#fff" stroke-width=".8"/><path d="M2.5 6h7M6 2.5c-1.5 2-1.5 5 0 7M6 2.5c1.5 2 1.5 5 0 7" fill="none" stroke="#fff" stroke-width=".7"/></svg>
        www.stepwise.com
      </li>
    </ul>
    <address class="address">Street Name, City Name<br>State Zip Code</address>
  </section>

  <section class="card card--back" aria-label="Business card back">
    <div class="brand-name">stepwise</div>
    <div class="web-line">www.stepwise.com</div>
  </section>
</body>
</html>
```